New Meal Prep Flyer for New Package Deals

We are looking for a design that displays our new packages that we offer. If you take a look at our website www.brambleforkmeals.com, and click on packages , you'll see the way we display them currently . We would like something similar to that in style . The first package is called "Horizon" and this package will be a 1 week package (7 days ), 2 meals a day, for a price of $195.00. The second package is called "Amber" and this package will be a 3 week package (21 days) 2 meals per day, for a price of $546.00 , the third package is a 6 week+ package (45 days), and it is called "Evergreen" , 2 meals per day , and the price is $1080.00 .
For the Amber Package , can you put next to it "Save $42.00!"
For the Evergreen Package, can you put next to it "Save $180!"
We also want our logo on the flyer (see attached), and we are just looking for a 1 page flyer , 8 1/2 x 11.

```html
<!DOCTYPE html>
<html lang="en">
<head>
<meta charset="utf-8">
<title>Bramblefork Meal Prep Packages Flyer</title>
<link rel="stylesheet" href="https://fonts.googleapis.com/css2?family=Lato:wght@400;700;900&display=swap">
<style>
  :root {
    --stage: #8e8e8e;
    --paper: #ffffff;
    --ink: #2b2b2b;
    --charcoal: #262626;
    --green: #76b82a;
    --green-bright: #8fd13a;
    --pill: #ffffff;
  }
  * { box-sizing: border-box; margin: 0; padding: 0; }
  html, body { width: 1200px; height: 900px; overflow: hidden; }
  body {
    background: var(--stage);
    font-family: "Lato", Arial, sans-serif;
    position: relative;
  }
  .flyer {
    position: absolute;
    left: 270px; top: 23px;
    width: 660px; height: 854px;
    background: var(--paper);
    overflow: hidden;
  }
  .top-band {
    position: absolute; left: 0; top: 26px;
    width: 660px; height: 332px;
    background: var(--charcoal);
  }
  .photo-frame {
    position: absolute; left: 44px; top: 39px;
    width: 590px; height: 423px;
    background: var(--green);
    padding: 10px;
  }
  .photo-grid {
    width: 100%; height: 100%;
    background: var(--paper);
    display: grid;
    grid-template-columns: 1fr 1fr;
    grid-template-rows: 1fr 1fr;
    gap: 5px;
  }
  .photo { width: 100%; height: 100%; }
  .photo-pizza { background: radial-gradient(ellipse at 45% 50%, #d98a3c 0%, #c2703a 40%, #d9d2c4 75%, #c9c2b6 100%); }
  .photo-veg { background: radial-gradient(ellipse at 50% 50%, #e7a13c 0%, #5d9c2c 40%, #f1efe9 72%, #cfd3d6 100%); }
  .photo-truffles { background: radial-gradient(ellipse at 50% 60%, #efe6dc 0%, #c7ab90 45%, #6b4a34 100%); }
  .photo-wraps { background: radial-gradient(ellipse at 50% 50%, #c9413a 0%, #d8b98d 40%, #cfc3ad 70%, #b8b3aa 100%); }

  .brand-box {
    position: absolute; left: 180px; top: 195px;
    width: 306px; height: 84px;
    background: var(--paper);
    border: 3px solid var(--green);
    display: flex; flex-direction: column;
    align-items: center; justify-content: center;
    gap: 4px;
  }
  .brand-name {
    font-weight: 900;
    font-size: 33px;
    letter-spacing: 1px;
    color: var(--green);
    line-height: 1;
  }
  .brand-tagline {
    font-weight: 700;
    font-size: 13px;
    letter-spacing: 1px;
    color: var(--green);
  }

  .packages {
    position: absolute; top: 494px; left: 0;
    width: 660px; height: 241px;
  }
  .package {
    position: absolute; top: 0;
    width: 155px; height: 241px;
    color: var(--paper);
    text-align: center;
  }
  .package svg.package-shape { position: absolute; inset: 0; }
  .package--horizon { left: 72px; }
  .package--amber { left: 259px; }
  .package--evergreen { left: 434px; top: 6px; }
  .package-name {
    position: relative;
    font-weight: 900;
    font-size: 17px;
    padding-top: 10px;
    letter-spacing: 0.3px;
    text-transform: uppercase;
  }
  .package-details {
    position: absolute; left: 0; right: 0; top: 108px;
  }
  .validity { font-size: 19px; font-weight: 400; letter-spacing: 0.5px; line-height: 1.1; }
  .duration { font-size: 14px; margin-top: 2px; }
  .price {
    display: inline-block;
    margin-top: 8px;
    background: var(--pill);
    color: var(--ink);
    font-size: 11px;
    padding: 3px 14px;
    border-radius: 10px;
  }
  .meals { font-size: 13px; margin-top: 8px; }
  .savings {
    font-size: 13px;
    font-weight: 900;
    letter-spacing: 0.5px;
    margin-top: 6px;
  }
  .package--amber .savings { color: var(--paper); }
  .package--evergreen .savings { color: var(--green-bright); }

  .app-bar {
    position: absolute; left: 0; top: 762px;
    width: 560px; height: 44px;
    background: var(--charcoal);
    color: var(--paper);
    font-size: 16px;
    letter-spacing: 0.5px;
    display: flex; align-items: center;
    padding-left: 78px;
  }
  .web-bar {
    position: absolute; left: 0; top: 818px;
    width: 660px; height: 30px;
    background: var(--green);
    color: var(--paper);
    font-size: 13px;
    letter-spacing: 4px;
    display: flex; align-items: center;
    padding-left: 80px;
  }
  .plate {
    position: absolute; left: 420px; top: 756px;
    width: 210px; height: 58px;
    background: var(--paper);
    border-radius: 6px;
    transform: rotate(-6deg);
    box-shadow: 0 3px 8px rgba(0,0,0,0.35);
    padding: 12px 30px;
  }
  .plate-food {
    width: 100%; height: 100%;
    border-radius: 14px;
    background: linear-gradient(90deg, #b5602f 0%, #7fa13a 35%, #e8dcc0 55%, #7fa13a 75%, #b5602f 100%);
  }
</style>
</head>
<body>
  <main class="flyer">
    <div class="top-band"></div>

    <section class="photo-frame">
      <div class="photo-grid">
        <div class="photo photo-pizza" role="img" aria-label="Thin-crust pizza cut into slices on parchment"></div>
        <div class="photo photo-veg" role="img" aria-label="Bowl of mixed stir-fried vegetables"></div>
        <div class="photo photo-truffles" role="img" aria-label="Stack of cocoa-dusted white truffles with cake behind"></div>
        <div class="photo photo-wraps" role="img" aria-label="Grilled wraps filled with chicken and vegetables"></div>
      </div>
    </section>

    <div class="brand-box">
      <div class="brand-name">BRAMBLEFORK</div>
      <div class="brand-tagline">HEALTHY KITCHEN | MEAL PREP</div>
    </div>

    <section class="packages">
      <article class="package package--horizon">
        <svg class="package-shape" width="155" height="241" viewBox="0 0 155 241">
          <rect x="0" y="0" width="155" height="241" rx="14" fill="var(--charcoal)"/>
          <path d="M0 46 H98 A24 24 0 0 1 98 94 H72" fill="none" stroke="var(--paper)" stroke-width="13" stroke-linecap="round"/>
        </svg>
        <h2 class="package-name">Horizon</h2>
        <div class="package-details">
          <div class="validity">VALIDITY</div>
          <div class="duration">1WEEK (7 DAYS )</div>
          <div class="price">price - $195.00</div>
          <div class="meals">2 MEALS A DAY</div>
        </div>
      </article>

      <article class="package package--amber">
        <svg class="package-shape" width="155" height="241" viewBox="0 0 155 241">
          <rect x="0" y="0" width="155" height="241" rx="14" fill="var(--green)"/>
          <path d="M0 46 H98 A24 24 0 0 1 98 94 H72" fill="none" stroke="var(--paper)" stroke-width="13" stroke-linecap="round"/>
        </svg>
        <h2 class="package-name">Amber</h2>
        <div class="package-details">
          <div class="validity">VALIDITY</div>
          <div class="duration">3WEEK (21 DAYS )</div>
          <div class="price">price - $546.00</div>
          <div class="meals">2 MEALS A DAY</div>
          <div class="savings">Save $42.00!</div>
        </div>
      </article>

      <article class="package package--evergreen">
        <svg class="package-shape" width="155" height="241" viewBox="0 0 155 241">
          <rect x="0" y="0" width="155" height="235" rx="14" fill="var(--charcoal)"/>
          <path d="M0 46 H98 A24 24 0 0 1 98 94 H72" fill="none" stroke="var(--paper)" stroke-width="13" stroke-linecap="round"/>
        </svg>
        <h2 class="package-name">Evergreen</h2>
        <div class="package-details">
          <div class="validity">VALIDITY</div>
          <div class="duration">6WEEK (45DAYS )</div>
          <div class="price">price - $1080.00</div>
          <div class="meals">2 MEALS A DAY</div>
          <div class="savings">Save $180!</div>
        </div>
      </article>
    </section>

    <div class="app-bar">ORDER FOOD EASILY ON OUR APP</div>
    <div class="web-bar">www.brambleforkmeals.com</div>

    <div class="plate">
      <div class="plate-food" role="img" aria-label="Loaded flatbread topped with greens and sauce"></div>
    </div>
  </main>
</body>
</html>
```